Roaming outings business card

please see website
www.roamingoutings.comau

info needed on card
Keiran Voss
Ph
email
Adventure Riding GPS trails

please use my logo and colours off my site

Business

Keiran Voss
keiran@roamingoutings.com

```html
<!DOCTYPE html>
<html lang="en">
<head>
<meta charset="utf-8">
<title>Roaming Outings – Business Card</title>
<link rel="stylesheet" href="https://fonts.googleapis.com/css2?family=Source+Sans+3:ital,wght@0,400;0,600;0,700;1,600&display=swap">
<style>
  :root {
    --page-bg: #4a4a4a;
    --card-bg: #f7f7f7;
    --ink: #111111;
    --ink-soft: #3a3a3a;
    --accent-yellow: #f5cc12;
    --corner-black: #050505;
    --edge-white: #ffffff;
  }
  * { margin: 0; padding: 0; box-sizing: border-box; }
  html, body {
    width: 1200px;
    height: 750px;
    overflow: hidden;
    background: var(--page-bg);
    font-family: "Source Sans 3", Arial, sans-serif;
  }
  .business-card {
    position: absolute;
    left: 145px;
    top: 115px;
    width: 910px;
    height: 520px;
    background: var(--card-bg);
    overflow: hidden;
  }
  .card-corners {
    position: absolute;
    inset: 0;
    width: 100%;
    height: 100%;
  }
  .brand {
    position: absolute;
    right: 40px;
    top: 82px;
    display: flex;
    align-items: center;
    gap: 16px;
  }
  .brand-dot {
    width: 26px;
    height: 26px;
    border-radius: 50%;
    background: var(--accent-yellow);
  }
  .brand-name {
    font-size: 44px;
    font-weight: 700;
    color: var(--ink);
    line-height: 1;
  }
  .contact-block {
    position: absolute;
    left: 40px;
    top: 280px;
  }
  .person-name {
    font-size: 33px;
    font-weight: 600;
    color: var(--ink);
    margin-bottom: 14px;
  }
  .contact-list { list-style: none; }
  .contact-item {
    display: flex;
    align-items: center;
    gap: 12px;
    font-size: 21px;
    color: var(--ink-soft);
    height: 36px;
  }
  .contact-icon { width: 24px; height: 24px; flex: none; }
  .tagline {
    margin-top: 10px;
    font-size: 25px;
    font-style: italic;
    font-weight: 600;
    color: var(--ink-soft);
    letter-spacing: 0.5px;
  }
</style>
</head>
<body>
  <div class="business-card">
    <svg class="card-corners" viewBox="0 0 576 329" preserveAspectRatio="none" aria-hidden="true">
      <path d="M0,0 H132 C62,20 10,72 0,136 Z" fill="var(--corner-black)"/>
      <path d="M132,0 C62,20 10,72 0,136" fill="none" stroke="var(--edge-white)" stroke-width="5"/>
      <path d="M127,1 C60,22 9,72 1,128" fill="none" stroke="var(--accent-yellow)" stroke-width="3.5"/>
      <path d="M576,193 C560,250 512,300 444,329 H576 Z" fill="var(--corner-black)"/>
      <path d="M576,193 C560,250 512,300 444,329" fill="none" stroke="var(--edge-white)" stroke-width="5"/>
      <path d="M572,200 C555,252 508,300 450,328" fill="none" stroke="var(--accent-yellow)" stroke-width="3.5"/>
    </svg>

    <div class="brand">
      <span class="brand-dot"></span>
      <span class="brand-name">Roaming Outings</span>
    </div>

    <div class="contact-block">
      <h1 class="person-name">Keiran Voss</h1>
      <ul class="contact-list">
        <li class="contact-item">
          <svg class="contact-icon" viewBox="0 0 24 24" aria-hidden="true"><path fill="var(--ink)" d="M6.6 10.8a15 15 0 0 0 6.6 6.6l2.2-2.2c.3-.3.7-.4 1-.2 1.1.4 2.3.6 3.6.6.6 0 1 .4 1 1V20c0 .6-.4 1-1 1A17 17 0 0 1 3 4c0-.6.4-1 1-1h3.5c.6 0 1 .4 1 1 0 1.3.2 2.5.6 3.6.1.3 0 .7-.2 1z"/></svg>
          555 210 7486
        </li>
        <li class="contact-item">
          <svg class="contact-icon" viewBox="0 0 24 24" aria-hidden="true"><rect x="2" y="5" width="20" height="14" rx="1" fill="var(--ink)"/><path d="M3 6l9 7 9-7" fill="none" stroke="var(--card-bg)" stroke-width="1.6"/></svg>
          keiran@roamingoutings.com
        </li>
        <li class="contact-item">
          <svg class="contact-icon" viewBox="0 0 24 24" aria-hidden="true"><circle cx="12" cy="12" r="10" fill="var(--ink)"/><path d="M12 2v20M2 12h20M5 6.5c4 2 10 2 14 0M5 17.5c4-2 10-2 14 0" fill="none" stroke="var(--card-bg)" stroke-width="1.3"/><ellipse cx="12" cy="12" rx="4.5" ry="10" fill="none" stroke="var(--card-bg)" stroke-width="1.3"/></svg>
          www.roamingoutings.com.au
        </li>
      </ul>
      <p class="tagline">Adventure Riding GPS trails</p>
    </div>
  </div>
</body>
</html>
```